Business Card Design Project

need some business cards with the logo provided. I am a manufacturing jeweller that make high end quality jewellery in silver, gold and platinum and some amazing colored stones and of course diamonds.
Updates

Project Deadline Extended
Reason: I didn't choose this specific deadline and not sure why it was so short. A team member of craft huddle helped as i am not the best on computers. (-: (wasn't asked about the dead line)

Target Market(s)

Adults based between 20 to 60 and have budgets between $5000 - $100 000

Industry/Entity Type

Business

Colors

Designer to choose colors to be used in the design.

Requirements
Must have
• All in the front of business card
LOGO provided
My name: Corinne Walbeck
Job: Manufacturing jeweller
Phone number: 047 215 3904
Email: walcor@fernmail.example and the pagewave logo
this all in the back:
description of what i do : Hand Made Jewellery
new designs, remodelling, bridal jewellery, pearl re-threading and repairs
PO Box 1735, Kestrel Bay, 6291
Should not have
• Any diamond shapes or diamond rings or gemstones.

```html
<!DOCTYPE html>
<html lang="en">
<head>
<meta charset="utf-8">
<title>Orvane Jewellers – Business Card</title>
<link rel="stylesheet" href="https://fonts.googleapis.com/css2?family=Questrial&display=swap">
<style>
  :root {
    --backdrop: #2b2b2c;
    --gold: #95803c;
    --band: #262626;
    --gold-foil: #c9a93e;
    --paper-light: #f2f2f2;
    --paper-shade: #dcdcdc;
    --ink: #1c1c1c;
    --silver: #9a9a9a;
    --rule: #555555;
  }
  * { box-sizing: border-box; margin: 0; padding: 0; }
  html, body {
    width: 1200px;
    height: 799px;
    overflow: hidden;
    background: var(--backdrop);
    font-family: "Questrial", "Century Gothic", sans-serif;
  }
  .canvas {
    position: relative;
    width: 1200px;
    height: 799px;
    display: flex;
    align-items: center;
    justify-content: center;
    gap: 60px;
  }
  .card {
    position: relative;
    width: 520px;
    height: 300px;
    border-radius: 0 56px 0 56px;
    overflow: hidden;
    box-shadow: 0 10px 28px rgba(0,0,0,.45);
  }

  /* Front */
  .card--front { background: var(--gold); }
  .card__band {
    position: absolute;
    top: 0;
    bottom: 0;
    left: 286px;
    width: 124px;
    background: var(--band);
  }
  .card__band .brand {
    position: absolute;
    left: 0;
    right: 0;
    bottom: 52px;
    text-align: center;
    color: var(--gold-foil);
  }
  .card__band .brand__name { font-size: 22px; letter-spacing: 2px; }
  .card__band .brand__sub { font-size: 7px; letter-spacing: 3px; }

  .brand__name {
    display: block;
    line-height: 1;
  }
  .brand__sub {
    display: block;
    margin-top: 5px;
  }

  /* Back */
  .card--back {
    background: linear-gradient(135deg, var(--paper-light) 0%, var(--paper-shade) 100%);
    color: var(--ink);
  }
  .card--back .brand {
    position: absolute;
    top: 34px;
    right: 44px;
    text-align: center;
    color: var(--silver);
  }
  .card--back .brand__name { font-size: 40px; letter-spacing: 4px; }
  .card--back .brand__sub { font-size: 9px; letter-spacing: 6px; }

  .services {
    position: absolute;
    top: 118px;
    right: 290px;
    text-align: right;
    list-style: none;
    font-size: 15px;
    line-height: 19px;
  }
  .services__title { margin-bottom: 4px; }
  .services__item::after {
    content: "";
    display: inline-block;
    margin-left: 7px;
    border-top: 3px solid transparent;
    border-bottom: 3px solid transparent;
    border-right: 5px solid var(--ink);
    vertical-align: middle;
  }
  .divider {
    position: absolute;
    left: 250px;
    top: 176px;
    width: 1px;
    height: 64px;
    background: var(--rule);
  }
  .contact {
    position: absolute;
    left: 266px;
    top: 142px;
    font-style: normal;
    font-size: 15px;
    line-height: 19px;
  }
  .contact__name {
    font-size: 22px;
    margin-bottom: 12px;
    padding-left: 20px;
  }
</style>
</head>
<body>
<main class="canvas">
  <section class="card card--front" aria-label="Card front">
    <div class="card__band">
      <div class="brand">
        <span class="brand__name">ORVANE</span>
        <span class="brand__sub">JEWELLERS</span>
      </div>
    </div>
  </section>

  <section class="card card--back" aria-label="Card back">
    <div class="brand">
      <span class="brand__name">ORVANE</span>
      <span class="brand__sub">JEWELLERS</span>
    </div>
    <ul class="services">
      <li class="services__title">Hand Made Jewellery</li>
      <li class="services__item">new designs</li>
      <li class="services__item">remodelling</li>
      <li class="services__item">bridal jewellery</li>
      <li class="services__item">pearl re-threading</li>
      <li class="services__item">repairs</li>
    </ul>
    <div class="divider"></div>
    <address class="contact">
      <p class="contact__name">Corinne Walbeck</p>
      <p>Manufacturing jeweller</p>
      <p>047 215 3904</p>
      <p>walcor@fernmail.example</p>
      <p>PO Box 1735,</p>
      <p>Kestrel Bay, 6291</p>
    </address>
  </section>
</main>
</body>
</html>
```